coaching agenda

Please redesign the brochure attached in a more modern/trendy out look. I want something completely different to what is attached but using the same colours and logo.

```html
<!DOCTYPE html>
<html lang="en">
<head>
<meta charset="utf-8">
<title>Coaching Session – June 2018</title>
<link href="https://fonts.googleapis.com/css2?family=Roboto:wght@400;500;700&family=Roboto+Condensed:wght@400;700&display=swap" rel="stylesheet">
<style>
:root{
  --blue:#1f9bd7;
  --blue-soft:rgba(64,170,222,.78);
  --ink:#1d1d1f;
  --charcoal:#333a40;
  --paper:#ffffff;
  --backdrop:#d9dbdd;
}
*{box-sizing:border-box;margin:0;padding:0}
html,body{width:1200px;height:844px;overflow:hidden;background:var(--backdrop)}
body{position:relative;font-family:"Roboto",Arial,sans-serif;color:var(--ink)}
.page{position:absolute;top:42px;width:536px;height:756px;background:var(--paper);overflow:hidden}
.page--front{left:48px}
.page--back{left:618px}
.abs{position:absolute}

/* front page */
.hero{left:0;top:0;width:536px;height:243px;background:linear-gradient(160deg,#eef2f4 0%,#c9d6df 45%,#7c8c98 75%,#4a4f57 100%)}
.brand{left:24px;top:18px;display:flex;align-items:center;gap:8px}
.brand__mark{width:14px;height:14px;background:var(--blue)}
.brand__name{font-family:"Roboto Condensed",sans-serif;font-weight:700;font-size:22px;color:var(--charcoal)}
.brand__legal{left:24px;top:46px;font-size:7px;color:var(--charcoal)}
.issue{right:76px;top:26px;text-align:center;font-family:"Roboto Condensed",sans-serif}
.issue__month{font-size:28px;color:var(--ink);line-height:1}
.issue__year{font-size:42px;font-weight:700;color:var(--blue);line-height:1.05}
.title-band{left:0;top:168px;width:374px;height:45px;background:var(--blue-soft);color:#fff;font-family:"Roboto Condensed",sans-serif;font-weight:700;font-size:36px;line-height:45px;padding-left:21px;letter-spacing:.5px}
.band{left:0;width:536px;height:37px;background:var(--blue);color:#fff;font-family:"Roboto Condensed",sans-serif;font-weight:700;font-size:22px;line-height:37px}
.band--front{top:243px;text-align:center;padding-right:44px}
.q-list{list-style:none}
.q-list li{position:absolute;left:0;font-size:11px;font-weight:500;white-space:nowrap}
.q-list .num{position:absolute;left:-30px;color:var(--blue);font-size:13px;font-weight:400;top:-2px}
.tab{left:0;top:397px;width:148px;height:35px;background:var(--blue);color:#fff;font-family:"Roboto Condensed",sans-serif;font-size:22px;line-height:35px;padding-left:40px}
.tab-title{left:152px;top:404px;font-size:18px;font-weight:500;letter-spacing:1.2px}
.lead{left:66px;top:444px;font-size:17px;font-weight:500}
.bullets{list-style:none}
.bullets li{position:absolute;font-size:12.5px;line-height:15px}
.bullets li::before{content:"";position:absolute;left:-28px;top:3px;width:9px;height:9px;background:var(--blue)}
.footer-bar{left:0;bottom:0;width:536px;height:10px;background:var(--blue)}
.footer-bar::before{content:"";position:absolute;left:0;top:0;width:283px;height:10px;background:var(--charcoal)}

/* back page */
.top-bar{left:0;top:0;width:536px;height:13px;background:var(--blue)}
.band--back{top:288px;padding-left:67px;font-size:23px}
.tips{list-style:none}
.tips li{position:absolute;left:67px;width:450px;font-size:11px;font-weight:700;line-height:14px;letter-spacing:.2px}
.tips svg{position:absolute;left:-43px;top:-2px}
.n-list{list-style:none}
.n-list li{position:absolute;left:65px;width:460px;font-size:12.5px;line-height:15px}
.n-list .num{position:absolute;left-adjust:0;left:-29px;color:var(--blue);font-size:14px}
</style>
</head>
<body>

<section class="page page--front">
  <div class="abs hero" role="img" aria-label="Photo of a presenter speaking to a seated audience in a bright training room"></div>
  <div class="abs brand"><span class="brand__mark"></span><span class="brand__name">Harlow Reed</span></div>
  <div class="abs brand__legal">Salesmentor Group Pty Ltd</div>
  <div class="abs issue"><div class="issue__month">JUNE</div><div class="issue__year">2018</div></div>
  <div class="abs title-band">COACHING SESSION</div>
  <div class="abs band band--front">Yesterday – Today – Tomorrow</div>

  <ol class="q-list">
    <li style="left:66px;top:296px"><span class="num">1.</span>How many appraisals/listing presentations are booked in your diary for this week?</li>
    <li style="left:66px;top:320px"><span class="num">2.</span>How many appraisals/listing presentations are booked in your diary for next week?</li>
    <li style="left:66px;top:343px"><span class="num">3.</span>How many second viewings/private viewings are booked in your diary for this week?</li>
    <li style="left:66px;top:365px"><span class="num">4.</span>How many listings will you launch this week?</li>
  </ol>

  <div class="abs tab">2018/2019</div>
  <div class="abs tab-title">Productivity Gets</div>
  <div class="abs lead">There’s more to it than numbers:</div>

  <ul class="bullets">
    <li style="left:66px;top:477px">Increase in market share in your core area</li>
    <li style="left:66px;top:506px">Increase in commission rates</li>
    <li style="left:66px;top:536px">Relationships [ data base growth]- future sellers</li>
    <li style="left:66px;top:564px">Relationships [ data base growth] – buyer prospects</li>
    <li style="left:66px;top:592px">Number of appointments/appraisals booked each week</li>
    <li style="left:66px;top:618px">Listing pipeline growth</li>
    <li style="left:66px;top:645px;width:370px">Skills development –is an opportunity - you can’t be defined as not knowing what to do. Be specific. You can’t become a better closer if you don’t have people to close on!!</li>
    <li style="left:66px;top:701px">Managing free time – you can’t be defined by time</li>
  </ul>
  <div class="abs footer-bar"></div>
</section>

<section class="page page--back">
  <div class="abs top-bar"></div>
  <ul class="bullets">
    <li style="left:67px;top:28px">Time is an opportunity</li>
    <li style="left:67px;top:56px;width:380px">Service charter – there is opportunity in service – repeat/ referrals/the future seller calls “you in”</li>
    <li style="left:67px;top:97px">Know your data base system – data base is an opportunity</li>
    <li style="left:67px;top:126px;width:400px">Service charter – there is opportunity in service – repeat/referrals/ the future seller calls “you in”</li>
    <li style="left:67px;top:166px">Health &amp; energy leads to better recovery</li>
    <li style="left:67px;top:192px">Family &amp; self- breaks</li>
    <li style="left:67px;top:217px">Self-time</li>
    <li style="left:67px;top:239px">Milestones/benchmarks</li>
    <li style="left:67px;top:261px">Wealth creation</li>
  </ul>

  <div class="abs band band--back">Today onwards [12/6/18]</div>

  <ul class="tips">
    <li style="top:338px">
      <svg width="26" height="26" viewBox="0 0 26 26" fill="none" stroke="#1f9bd7" stroke-width="1.6"><path d="M4 22 L18 8 M16 4 a5 5 0 0 0 6 6 L20 12 L14 6 Z M4 4 L10 10 M8 4 L4 8 L9 13 L13 9 Z M15 15 L22 22"/></svg>
      Build the listing pipeline so you have shock coming to market when the sun shines again</li>
    <li style="top:386px">
      <svg width="26" height="26" viewBox="0 0 26 26" fill="none" stroke="#1f9bd7" stroke-width="1.6"><path d="M3 23 H23 M3 23 V3 M7 19 V14 M12 19 V11 M17 19 V8 M6 12 L20 4 M16 4 H20 V8"/></svg>
      Don’t wait until the usual “spring selling session” promo’s start to start looking for listings.</li>
    <li style="top:432px">
      <svg width="30" height="30" viewBox="0 0 30 30" fill="none" stroke="#1f9bd7" stroke-width="1.6"><circle cx="14" cy="16" r="12"/><circle cx="14" cy="16" r="8"/><circle cx="14" cy="16" r="4"/><path d="M14 16 L25 5 M22 4 H26 V8"/></svg>
      Get the &nbsp;jump on your competition by having your July to December profile building campaign set in place now &amp; make sure it is fully funded so you don’t lose profile momentum.</li>
  </ul>

  <ol class="n-list">
    <li style="top:493px"><span class="num">1.</span>What went well this month?</li>
    <li style="top:522px"><span class="num">2.</span>Did you convert good days into good weeks, good weeks into a good month?</li>
    <li style="top:550px"><span class="num">3.</span>How organised were you last week?</li>
    <li style="top:579px;width:400px"><span class="num">4.</span>What ideas, actions, processes, systems and motivations have you introduced into your business during the last thirty days?</li>
    <li style="top:621px"><span class="num">5.</span>What systems do you need to implement to create a smoother work flow?</li>
    <li style="top:651px"><span class="num">6.</span>Are you pursuing what you believe in?</li>
    <li style="top:680px"><span class="num">7.</span>At what time of the day are you running at your true potential?</li>
    <li style="top:707px"><span class="num">8.</span>What have been your numbers for May?</li>
  </ol>
  <div class="abs footer-bar"></div>
</section>

</body>
</html>
```